CVA Business Card

I would like to create a busienss card for the high school teachers. Our school colors are red and black and our mascot is the bulldog. In addition, to our school address and contact information, I would like to add our twitter account and fb account. We also have a school website. Somewhere I would like to incorporate our school wide expectations: Be Safe, Be Respectful, Be Responsible and Be a Learner.

Thornbury Academy
2424 Pinegate
Thornbury, KS 67302
620.418.7093
620.418.7094(fax)
www.thornburylearning.example
www.facebook.example/ThornburyOtters
twitter.example/ThornburyKsDist or @ThornburyKsDist
Teacher Name:
Teacher Email:

I would like to personalize each card with the teacher name and their email.

I would also like to use Otter Circle – Roots.Now.Ahead

                                      Front Side of Card:  Teacher and School Contact Information

Back Side of Card:  Otter Circle -several designers have asked about this-our school is trying to promote that we are a family trying to promote a positive climate.  We also want to add Roots.Now.Ahead with information that might pertain to the past, present, or future to keep people coming back to our website or facebook.

At first I mentioned that I wanted to use the bulldog as the graphic because it is our mascot, now I am changing my mind about maybe something more student centered like a group of stick figures circle together or arms around each other symbolizing that we are working together to accomplish our goal.

I need to make sure that our school wide expectations are also incorporated:

Be Safe.Be Respectful.Be Responsible.Be A Learner

Target Market(s)

9-12 students and professionals

Industry/Entity Type

High School

Requirements
Must have
• Contact information
Otter Circle with Past, Present and Future Incorporated
Two sided business card
Side #1 Contact Info + graphic (might use bulldog that I attached however not sure if I like it)
Side #2 Otter Circle with Past, Present and Future (incorporate a graphic that symbolizes togetherness or working together.

```html
<!DOCTYPE html>
<html lang="en">
<head>
<meta charset="utf-8">
<title>Thornbury Academy – Teacher Business Card</title>
<link rel="stylesheet" href="https://fonts.googleapis.com/css2?family=Audiowide&family=Lato:wght@300;400&family=Tinos&display=swap">
<style>
  :root {
    --card-black: #000000;
    --card-red: #f1100f;
    --card-white: #ffffff;
    --slogan-red: #e0141a;
    --slogan-edge: #3a0b0b;
    --school-yellow: #f4ea4b;
    --text-white: #ffffff;
    --mascot-light: #e9e9e9;
    --mascot-dark: #6e6e6e;
    --web-green: #3ec43a;
    --fb-blue: #2a5aa8;
    --tw-cyan: #2bb7e6;
  }
  html, body {
    margin: 0;
    padding: 0;
    width: 1200px;
    height: 741px;
    overflow: hidden;
    background: var(--card-white);
  }
  .card {
    position: relative;
    width: 1200px;
    height: 741px;
    overflow: hidden;
    background: var(--card-white);
    font-family: "Lato", sans-serif;
  }
  .card-panels {
    position: absolute;
    inset: 0;
  }
  .mascot-art {
    position: absolute;
    left: 705px;
    top: 255px;
    width: 495px;
    height: 486px;
    border-radius: 46% 40% 8% 10% / 30% 30% 6% 6%;
    background: radial-gradient(ellipse at 45% 45%, var(--mascot-light) 0%, #bdbdbd 60%, var(--mascot-dark) 100%);
    opacity: 0.75;
  }
  .expectations {
    position: absolute;
    left: 26px;
    top: 84px;
    width: 1150px;
    height: 50px;
  }
  .expectations text {
    font-family: "Audiowide", sans-serif;
    font-size: 40px;
    fill: var(--slogan-red);
    stroke: var(--slogan-edge);
    stroke-width: 1.6px;
    paint-order: stroke;
  }
  .contact {
    position: absolute;
    left: 29px;
    top: 262px;
    color: var(--text-white);
  }
  .school-name {
    margin: 0 0 14px;
    font-family: "Audiowide", sans-serif;
    font-weight: 400;
    font-size: 31px;
    letter-spacing: 1.5px;
    color: var(--school-yellow);
    line-height: 40px;
  }
  .school-details {
    margin: 0;
    font-weight: 300;
    font-size: 30px;
    letter-spacing: 1px;
    line-height: 39px;
  }
  .teacher {
    position: absolute;
    left: 29px;
    top: 490px;
    font-family: "Tinos", serif;
    font-size: 40px;
    line-height: 55px;
    color: var(--text-white);
  }
  .teacher p { margin: 0; }
  .channels {
    position: absolute;
    left: 29px;
    top: 649px;
    font-size: 20px;
    color: var(--text-white);
    font-weight: 400;
  }
  .channel-row {
    display: flex;
    align-items: center;
    height: 28px;
    margin-bottom: 13px;
  }
  .channel {
    display: inline-flex;
    align-items: center;
  }
  .channel-mark {
    display: inline-block;
    width: 26px;
    height: 26px;
    margin-right: 12px;
  }
  .mark-web { background: var(--web-green); }
  .mark-fb { background: var(--fb-blue); }
  .mark-tw { background: var(--tw-cyan); }
  .channel-divider { margin: 0 14px; }
</style>
</head>
<body>
<main class="card">
  <svg class="card-panels" width="1200" height="741" viewBox="0 0 1200 741" aria-hidden="true">
    <polygon points="0,0 748,0 704,741 0,741" fill="var(--card-red)"/>
    <polygon points="0,0 688,0 651,741 0,741" fill="var(--card-black)"/>
  </svg>

  <div class="mascot-art" role="img" aria-label="Standing bulldog mascot illustration in black and white"></div>

  <svg class="expectations" viewBox="0 0 1150 50" aria-label="Be Safe Be Respectful Be Responsible Be A Learner">
    <text x="0" y="40" textLength="1146" lengthAdjust="spacingAndGlyphs" transform="skewX(-12) translate(8 0)">BE SAFE BE RESPECTFUL BE RESPONSIBLE BE A LEARNER</text>
  </svg>

  <section class="contact">
    <h1 class="school-name">THORNBURY ACADEMY</h1>
    <p class="school-details">2424 Pinegate, Thornbury, KS 67302<br>620.418.7093 (tel)<br>620.418.7094(fax)</p>
  </section>

  <section class="teacher">
    <p class="teacher-name">Ms Laura Pennick</p>
    <p class="teacher-email">laura.pennick@edu.example</p>
  </section>

  <section class="channels">
    <div class="channel-row">
      <span class="channel"><span class="channel-mark mark-web"></span>www.thornburylearning.example</span>
    </div>
    <div class="channel-row">
      <span class="channel"><span class="channel-mark mark-fb"></span>@ThornburyOtters</span>
      <span class="channel-divider">I</span>
      <span class="channel"><span class="channel-mark mark-tw"></span>@ThornburyKsDist</span>
    </div>
  </section>
</main>
</body>
</html>
```